One Thumbnail for Online Shop for Slide Templates needed

We are selling Slide Templates and need therefore a thumbnail for our online shop.

You can use a stock photo, mock-ups or other design elements.

Format:
squared like 500 x 500
or wide like 1280 x 720

If you want to use a title, use:

"Graphs" ---> Title
"Slide template" ---> subtitle

Attachments:
- OLD: Our old thumbnail which I do not like
- Template: Slide pictures which you can use ( you can also copy them if you need more than these)
- Example: Some examples I found from other shops (please do not copy them exactly, only to show what I mean)

I received lots of designs until now but many are not what I have expected

Target Market(s)

E-Commerce

Industry/Entity Type

Shop

Font styles to use
Sans Serif

Requirements
Should not have
• Do NOT re-design one of the template.png (these are only examples, I will replace them later)

```html
<!DOCTYPE html>
<html lang="en">
<head>
<meta charset="utf-8">
<title>Graphs – Slide template</title>
<link rel="stylesheet" href="https://fonts.googleapis.com/css2?family=Arimo:wght@400;700&display=swap">
<style>
  :root {
    --bg-light: #e9e4dc;
    --bg-mid: #8a7f72;
    --bg-dark: #2a2724;
    --slide: #f7f8fa;
    --ink: #1c1c1c;
    --muted: #555a60;
    --blue: #4a8fd6;
    --navy: #1f4e82;
    --rule: #d5d9de;
    --gold: #ebb94c;
  }
  * { box-sizing: border-box; margin: 0; padding: 0; }
  html, body { width: 1200px; height: 750px; overflow: hidden; }
  body { font-family: "Arimo", Arial, sans-serif; position: relative; background: var(--bg-dark); }
  .scene-photo {
    position: absolute; inset: 0;
    background:
      radial-gradient(ellipse at 62% 30%, rgba(255,255,255,.55), rgba(255,255,255,0) 40%),
      linear-gradient(100deg, var(--bg-light) 0%, #d6cfc4 32%, var(--bg-mid) 60%, #4a4640 80%, var(--bg-dark) 100%);
  }
  .slide-card {
    position: absolute; background: var(--slide);
    box-shadow: 0 2px 8px rgba(0,0,0,.25);
  }
  .slide-card svg { display: block; }
  .card-charts { left: 42px; top: 290px; width: 340px; height: 191px; }
  .card-growth { left: 45px; top: 518px; width: 338px; height: 190px; }
  .card-ranking { left: 421px; top: 520px; width: 340px; height: 190px; }
  .t-title { font-weight: 700; font-size: 12.5px; fill: var(--ink); }
  .t-sub { font-size: 6.6px; fill: var(--muted); }
  .t-head { font-weight: 700; font-size: 5.6px; fill: var(--ink); }
  .t-tiny { font-size: 3.6px; fill: var(--muted); }
  .t-axis { font-size: 4.6px; fill: var(--muted); }
  .t-val { font-size: 5px; fill: var(--ink); }
  .t-in { font-size: 5px; fill: #fff; }
  .t-blue { font-size: 5.4px; fill: var(--blue); }
  .t-body { font-size: 4.4px; fill: var(--muted); }
  .bar { fill: var(--blue); }
  .bar-dark { fill: var(--navy); }
  .rule { stroke: var(--rule); stroke-width: .6; }
  .brand {
    position: absolute; left: 960px; top: 110px;
    display: flex; align-items: center; gap: 10px;
  }
  .brand-dot { width: 22px; height: 22px; border-radius: 50%; background: var(--gold); }
  .brand-name { font-weight: 700; font-size: 30px; color: var(--gold); }
</style>
</head>
<body>
  <div class="scene-photo" role="img" aria-label="Photo of a desk by a bright window with a desktop computer showing line and bar chart slides"></div>

  <section class="slide-card card-charts">
    <svg width="340" height="191" viewBox="0 0 340 191">
      <defs>
        <g id="chart-a">
          <rect class="bar" x="0" y="-14" width="5" height="6"/><rect class="bar-dark" x="0" y="-8" width="5" height="8"/>
          <rect class="bar" x="8" y="-26" width="5" height="12"/><rect class="bar-dark" x="8" y="-14" width="5" height="14"/>
          <rect class="bar" x="16" y="-40" width="5" height="20"/><rect class="bar-dark" x="16" y="-20" width="5" height="20"/>
          <rect class="bar" x="24" y="-43" width="5" height="21"/><rect class="bar-dark" x="24" y="-22" width="5" height="22"/>
          <rect class="bar" x="32" y="-38" width="5" height="20"/><rect class="bar-dark" x="32" y="-18" width="5" height="18"/>
          <rect class="bar" x="40" y="-38" width="5" height="18"/><rect class="bar-dark" x="40" y="-20" width="5" height="20"/>
          <rect class="bar" x="48" y="-36" width="5" height="18"/><rect class="bar-dark" x="48" y="-18" width="5" height="18"/>
          <rect class="bar" x="56" y="-36" width="5" height="18"/><rect class="bar-dark" x="56" y="-18" width="5" height="18"/>
          <rect class="bar" x="64" y="-34" width="5" height="18"/><rect class="bar-dark" x="64" y="-16" width="5" height="16"/>
          <rect class="bar" x="72" y="-24" width="5" height="12"/><rect class="bar-dark" x="72" y="-12" width="5" height="12"/>
          <rect class="bar" x="80" y="-30" width="5" height="14"/><rect class="bar-dark" x="80" y="-16" width="5" height="16"/>
          <rect class="bar" x="88" y="-32" width="5" height="16"/><rect class="bar-dark" x="88" y="-16" width="5" height="16"/>
        </g>
        <g id="chart-b">
          <rect class="bar" x="0" y="-26" width="5" height="12"/><rect class="bar-dark" x="0" y="-14" width="5" height="14"/>
          <rect class="bar" x="8" y="-22" width="5" height="10"/><rect class="bar-dark" x="8" y="-12" width="5" height="12"/>
          <rect class="bar" x="16" y="-43" width="5" height="15"/><rect class="bar-dark" x="16" y="-28" width="5" height="28"/>
          <rect class="bar" x="24" y="-40" width="5" height="20"/><rect class="bar-dark" x="24" y="-20" width="5" height="20"/>
          <rect class="bar" x="32" y="-26" width="5" height="12"/><rect class="bar-dark" x="32" y="-14" width="5" height="14"/>
          <rect class="bar" x="40" y="-20" width="5" height="8"/><rect class="bar-dark" x="40" y="-12" width="5" height="12"/>
          <rect class="bar" x="48" y="-24" width="5" height="12"/><rect class="bar-dark" x="48" y="-12" width="5" height="12"/>
          <rect class="bar" x="56" y="-30" width="5" height="14"/><rect class="bar-dark" x="56" y="-16" width="5" height="16"/>
          <rect class="bar" x="64" y="-24" width="5" height="12"/><rect class="bar-dark" x="64" y="-12" width="5" height="12"/>
          <rect class="bar" x="72" y="-28" width="5" height="14"/><rect class="bar-dark" x="72" y="-14" width="5" height="14"/>
          <rect class="bar" x="80" y="-22" width="5" height="10"/><rect class="bar-dark" x="80" y="-12" width="5" height="12"/>
          <rect class="bar" x="88" y="-24" width="5" height="10"/><rect class="bar-dark" x="88" y="-14" width="5" height="14"/>
        </g>
      </defs>
      <text class="t-title" x="170" y="18" text-anchor="middle">Lorem ipsum dolor sit amet</text>
      <text class="t-sub" x="170" y="30" text-anchor="middle">Lorem ipsum dolor sit amet, consectetuer adipiscing elit. Aenean commodo ligula eget dolor.</text>

      <text class="t-head" x="24" y="48">Lorem ipsum</text><text class="t-tiny" x="24" y="53">Lorem ipsum dolor sit amet, consectetur adipiscing elit</text>
      <use href="#chart-a" transform="translate(34,100)"/><line class="rule" x1="32" y1="100" x2="128" y2="100"/>
      <text class="t-head" x="132" y="48">Lorem ipsum</text><text class="t-tiny" x="132" y="53">Lorem ipsum dolor sit amet, consectetur adipiscing elit</text>
      <use href="#chart-b" transform="translate(142,100)"/><line class="rule" x1="140" y1="100" x2="236" y2="100"/>
      <text class="t-head" x="24" y="118">Lorem ipsum</text><text class="t-tiny" x="24" y="123">Lorem ipsum dolor sit amet, consectetur adipiscing elit</text>
      <use href="#chart-b" transform="translate(34,170)"/><line class="rule" x1="32" y1="170" x2="128" y2="170"/>
      <text class="t-head" x="132" y="118">Lorem ipsum</text><text class="t-tiny" x="132" y="123">Lorem ipsum dolor sit amet, consectetur adipiscing elit</text>
      <use href="#chart-a" transform="translate(142,170)"/><line class="rule" x1="140" y1="170" x2="236" y2="170"/>

      <g class="t-body">
        <text x="256" y="66">Lorem ipsum dolor sit amet,</text><text x="256" y="71">consetetur sadipscing elitr, sed</text><text x="256" y="76">diam nonumy eirmod tempor</text><text x="256" y="81">invidunt ut labore et dolore</text><text x="256" y="86">At vero eos et accusam</text>
        <text x="256" y="104">Lorem ipsum dolor sit amet,</text><text x="256" y="109">consetetur sadipscing elitr, sed</text><text x="256" y="114">diam nonumy eirmod tempor</text><text x="256" y="119">invidunt ut labore et dolore</text><text x="256" y="124">At vero eos et accusam</text>
        <text x="256" y="142">Lorem ipsum dolor sit amet,</text><text x="256" y="147">consetetur sadipscing elitr, sed</text><text x="256" y="152">diam nonumy eirmod tempor</text><text x="256" y="157">invidunt ut labore et dolore</text><text x="256" y="162">At vero eos et accusam</text>
        <text x="318" y="185">31</text>
      </g>
    </svg>
  </section>

  <section class="slide-card card-growth">
    <svg width="338" height="190" viewBox="0 0 338 190">
      <text class="t-title" x="169" y="18" text-anchor="middle">Lorem ipsum dolor sit amet</text>
      <text class="t-sub" x="169" y="30" text-anchor="middle">Lorem ipsum dolor sit amet, consectetuer adipiscing elit. Aenean commodo ligula eget dolor.</text>
      <g class="t-body">
        <text x="26" y="80">Lorem ipsum dolor sit amet,</text><text x="26" y="86">consetetur sadipscing elitr,</text><text x="26" y="92">sed diam nonumy eirmod</text><text x="26" y="98">tempor invidunt ut labore et</text><text x="26" y="104">dolore magna aliquyam erat.</text><text x="26" y="110">At vero eos et accusam</text>
        <text x="26" y="130">Lorem ipsum dolor sit amet,</text><text x="26" y="136">consetetur sadipscing elitr,</text><text x="26" y="142">sed diam nonumy eirmod</text><text x="26" y="148">tempor invidunt ut labore et</text><text x="26" y="154">dolore magna aliquyam erat.</text><text x="26" y="160">At vero eos et accusam</text>
        <text x="326" y="185" text-anchor="end">34</text>
      </g>
      <g class="bar">
        <rect x="103" y="138" width="9" height="29"/><rect x="118" y="136" width="9" height="31"/><rect x="134" y="130" width="9" height="37"/><rect x="149" y="121" width="9" height="46"/><rect x="165" y="119" width="9" height="48"/><rect x="180" y="114" width="9" height="53"/><rect x="195" y="110" width="9" height="57"/><rect x="211" y="103" width="9" height="64"/><rect x="226" y="103" width="9" height="64"/><rect x="242" y="99" width="9" height="68"/><rect x="257" y="97" width="9" height="70"/><rect x="273" y="92" width="9" height="75"/>
      </g>
      <g class="t-in" text-anchor="middle">
        <text x="107.5" y="152">13</text><text x="122.5" y="150">14</text><text x="138.5" y="147">17</text><text x="153.5" y="140">21</text><text x="169.5" y="139">22</text><text x="184.5" y="136">24</text><text x="199.5" y="134">26</text><text x="215.5" y="130">29</text><text x="230.5" y="130">29</text><text x="246.5" y="128">31</text><text x="261.5" y="127">32</text><text x="277.5" y="125">34</text>
      </g>
      <polyline fill="none" stroke="#9aa3ad" stroke-width=".7" points="107.5,122 122.5,119 138.5,111 153.5,100 169.5,97 184.5,92 199.5,87 215.5,79 230.5,79 246.5,73 261.5,68 277.5,68"/>
      <g fill="#fff" stroke="#9aa3ad" stroke-width=".6">
        <circle cx="107.5" cy="122" r="1.3"/><circle cx="122.5" cy="119" r="1.3"/><circle cx="138.5" cy="111" r="1.3"/><circle cx="153.5" cy="100" r="1.3"/><circle cx="169.5" cy="97" r="1.3"/><circle cx="184.5" cy="92" r="1.3"/><circle cx="199.5" cy="87" r="1.3"/><circle cx="215.5" cy="79" r="1.3"/><circle cx="230.5" cy="79" r="1.3"/><circle cx="246.5" cy="73" r="1.3"/><circle cx="261.5" cy="68" r="1.3"/><circle cx="277.5" cy="68" r="1.3"/>
      </g>
      <g class="t-val" text-anchor="middle">
        <text x="107.5" y="117">16</text><text x="122.5" y="114">17</text><text x="138.5" y="106">20</text><text x="153.5" y="95">24</text><text x="169.5" y="92">25</text><text x="184.5" y="87">27</text><text x="199.5" y="82">29</text><text x="215.5" y="74">32</text><text x="230.5" y="74">32</text><text x="246.5" y="68">34</text><text x="261.5" y="63">36</text><text x="277.5" y="63">36</text>
      </g>
      <text class="t-blue" x="286" y="70">Lorem ipsum</text>
      <text class="t-blue" x="286" y="123">Lorem ipsum</text>
      <g class="t-axis" text-anchor="middle">
        <text x="107.5" y="176">Text</text><text x="122.5" y="176">Text</text><text x="138.5" y="176">Text</text><text x="153.5" y="176">Text</text><text x="169.5" y="176">Text</text><text x="184.5" y="176">Text</text><text x="199.5" y="176">Text</text><text x="215.5" y="176">Text</text><text x="230.5" y="176">Text</text><text x="246.5" y="176">Text</text><text x="261.5" y="176">Text</text><text x="277.5" y="176">Text</text>
      </g>
    </svg>
  </section>

  <section class="slide-card card-ranking">
    <svg width="340" height="190" viewBox="0 0 340 190">
      <text class="t-title" x="170" y="18" text-anchor="middle">Lorem ipsum dolor sit amet</text>
      <text class="t-sub" x="170" y="30" text-anchor="middle">Lorem ipsum dolor sit amet, consectetuer adipiscing elit. Aenean commodo ligula eget dolor.</text>
      <text class="t-head" x="35" y="44">Lorem ipsum</text>
      <text class="t-body" x="35" y="50">Lorem ipsum dolor sit amet, consetetur sadipscing elitr, sed diam nonumy eirmod tempor</text>
      <text class="t-body" x="35" y="56">invidunt ut labore et dolore magna aliquyam erat, sed diam voluptua. At vero eos et accusam.</text>
      <g class="t-axis">
        <text x="22" y="68">Text</text><text x="22" y="78.5">Text</text><text x="22" y="89">Text</text><text x="22" y="99.5">Text</text><text x="22" y="110">Text</text><text x="22" y="120.5">Text</text><text x="22" y="131">Text</text><text x="22" y="141.5">Text</text><text x="22" y="152">Text</text><text x="22" y="162.5">Text</text>
      </g>
      <g class="rule">
        <line x1="35" y1="70.5" x2="158" y2="70.5"/><line x1="35" y1="81" x2="158" y2="81"/><line x1="35" y1="91.5" x2="158" y2="91.5"/><line x1="35" y1="102" x2="158" y2="102"/><line x1="35" y1="112.5" x2="158" y2="112.5"/><line x1="35" y1="123" x2="158" y2="123"/><line x1="35" y1="133.5" x2="158" y2="133.5"/><line x1="35" y1="144" x2="158" y2="144"/><line x1="35" y1="154.5" x2="158" y2="154.5"/>
        <line x1="168" y1="70.5" x2="245" y2="70.5"/><line x1="168" y1="81" x2="245" y2="81"/><line x1="168" y1="91.5" x2="245" y2="91.5"/><line x1="168" y1="102" x2="245" y2="102"/><line x1="168" y1="112.5" x2="245" y2="112.5"/><line x1="168" y1="123" x2="245" y2="123"/><line x1="168" y1="133.5" x2="245" y2="133.5"/><line x1="168" y1="144" x2="245" y2="144"/><line x1="168" y1="154.5" x2="245" y2="154.5"/>
      </g>
      <g class="bar-dark">
        <rect x="35" y="64" width="95" height="5"/><rect x="35" y="74.5" width="89" height="5"/><rect x="35" y="85" width="89" height="5"/><rect x="35" y="95.5" width="80" height="5"/><rect x="35" y="106" width="74" height="5"/><rect x="35" y="116.5" width="68" height="5"/><rect x="35" y="127" width="64" height="5"/><rect x="35" y="137.5" width="52" height="5"/><rect x="35" y="148" width="43" height="5"/><rect x="35" y="158.5" width="40" height="5"/>
      </g>
      <g class="t-val">
        <text x="133" y="68.5">31</text><text x="127" y="79">29</text><text x="127" y="89.5">29</text><text x="118" y="100">26</text><text x="112" y="110.5">24</text><text x="106" y="121">22</text><text x="102" y="131.5">21</text><text x="90" y="142">17</text><text x="81" y="152.5">14</text><text x="78" y="163">13</text>
      </g>
      <g class="bar">
        <rect x="197" y="64" width="22" height="5"/><rect x="197" y="74.5" width="29" height="5"/><rect x="183" y="85" width="14" height="5"/><rect x="190" y="95.5" width="7" height="5"/><rect x="197" y="106" width="22" height="5"/><rect x="197" y="116.5" width="22" height="5"/><rect x="197" y="127" width="7" height="5"/><rect x="190" y="137.5" width="7" height="5"/><rect x="197" y="148" width="29" height="5"/><rect x="197" y="158.5" width="14" height="5"/>
      </g>
      <g class="t-blue" style="font-size:4.6px">
        <text x="222" y="68.5">+3%</text><text x="229" y="79">+4%</text><text x="172" y="89.5">-2%</text><text x="178" y="100">-1%</text><text x="222" y="110.5">+3%</text><text x="222" y="121">+3%</text><text x="207" y="131.5">+1%</text><text x="178" y="142">-1%</text><text x="229" y="152.5">+4%</text><text x="214" y="163">+2%</text>
      </g>
      <g class="t-body">
        <text x="253" y="66">Lorem ipsum dolor sit amet,</text><text x="253" y="71">consetetur sadipscing elitr, sed</text><text x="253" y="76">diam nonumy eirmod tempor</text><text x="253" y="81">invidunt ut labore et dolore</text><text x="253" y="86">At vero eos et accusam</text>
        <text x="253" y="104">Lorem ipsum dolor sit amet,</text><text x="253" y="109">consetetur sadipscing elitr, sed</text><text x="253" y="114">diam nonumy eirmod tempor</text><text x="253" y="119">invidunt ut labore et dolore</text><text x="253" y="124">At vero eos et accusam</text>
        <text x="253" y="143">Lorem ipsum dolor sit amet,</text><text x="253" y="148">consetetur sadipscing elitr, sed</text><text x="253" y="153">diam nonumy eirmod tempor</text><text x="253" y="158">invidunt ut labore et dolore</text><text x="253" y="163">At vero eos et accusam</text>
        <text x="322" y="185">36</text>
      </g>
    </svg>
  </section>

  <div class="brand">
    <span class="brand-dot"></span>
    <span class="brand-name">Slidecraft</span>
  </div>
</body>
</html>
```